Homecare Information Flyer

We require a brochure/ leaflet to be created which would provide healthcare information to our staff and patients on the topic of- Pressure Ulcers. The document would ideally be 3 fold. It should include our Logo/ Company Information (Marrowby Staffing).

I have attached-
- Logo
- Text/ Visual images to be included.

Industry/Entity Type

Healthcare

```html
<!DOCTYPE html>
<html lang="en">
<head>
<meta charset="utf-8">
<title>Pressure Area Care – Marrowby Staffing leaflet</title>
<link href="https://fonts.googleapis.com/css2?family=Oswald:wght@300;400;500&family=Open+Sans:wght@400;600;700&display=swap" rel="stylesheet">
<style>
  :root {
    --green: #7ab842;
    --green-dark: #5e9a2c;
    --ink: #3a3a3a;
    --ink-soft: #5c5c5c;
    --paper: #ffffff;
    --backdrop: #efefec;
    --rule: #d9d9d9;
    --marker: #d9262b;
  }
  * { box-sizing: border-box; margin: 0; padding: 0; }
  html, body { width: 1200px; height: 1000px; overflow: hidden; }
  body {
    background: var(--backdrop);
    font-family: "Open Sans", Arial, sans-serif;
    color: var(--ink);
    position: relative;
  }

  /* Brand lockup */
  .brand { display: flex; align-items: center; gap: 10px; }
  .brand-dot { width: 22px; height: 22px; border-radius: 50%; background: var(--green); flex: none; }
  .brand-name { font-family: "Open Sans", Arial, sans-serif; font-weight: 700; color: var(--green-dark); white-space: nowrap; }
  .brand--hero { position: absolute; left: 60px; top: 70px; }
  .brand--hero .brand-dot { width: 56px; height: 56px; }
  .brand--hero .brand-name { font-size: 30px; }
  .brand--small .brand-dot { width: 16px; height: 16px; }
  .brand--small .brand-name { font-size: 12px; }

  /* Spreads */
  .spread {
    position: absolute;
    display: flex;
    height: 470px;
    background: var(--paper);
    box-shadow: 0 2px 10px rgba(0,0,0,.12);
  }
  .spread--inside { left: 480px; top: 20px; width: 690px; }
  .spread--outside { left: 710px; top: 506px; width: 460px; }
  .panel { position: relative; width: 230px; height: 100%; padding: 22px 18px 18px; overflow: hidden; }
  .panel + .panel { border-left: 1px solid #ececec; }

  /* Inside text */
  .tag {
    display: inline-block;
    background: var(--green);
    color: #fff;
    font-family: "Oswald", "Arial Narrow", sans-serif;
    font-weight: 400;
    font-size: 10.5px;
    line-height: 1;
    padding: 4px 10px 4px 18px;
    margin: 7px 0 3px -18px;
  }
  .copy { font-size: 7.6px; line-height: 1.45; color: var(--ink-soft); }
  .copy--lead { margin-bottom: 2px; }

  /* Locations panel */
  .locations-title { margin-top: 10px; }
  .pose-label {
    display: flex; align-items: center; gap: 5px;
    font-family: "Oswald", "Arial Narrow", sans-serif;
    font-size: 9px; color: var(--green-dark);
    margin: 10px 0 4px;
  }
  .pose-figure {
    height: 86px;
    background: linear-gradient(180deg, #fafafa, #eeeeee);
    border-radius: 3px;
  }

  /* Back panel */
  .panel--contact { padding: 0; }
  .contact-rotated {
    position: absolute;
    left: 50%; top: 50%;
    width: 430px;
    transform: translate(-50%, -50%) rotate(-90deg);
    padding: 0 20px;
  }
  .contact-rotated .brand { margin-bottom: 26px; }
  .contact-heading {
    font-family: "Oswald", "Arial Narrow", sans-serif;
    font-weight: 300;
    font-size: 30px;
    letter-spacing: 1px;
    color: var(--green);
    border-bottom: 1px solid var(--green);
    padding-bottom: 6px;
    margin-bottom: 14px;
  }
  .contact-name { font-family: "Oswald", "Arial Narrow", sans-serif; font-weight: 500; font-size: 17px; color: var(--ink); }
  .contact-role { font-family: "Oswald", "Arial Narrow", sans-serif; font-weight: 300; font-size: 14px; color: var(--ink-soft); margin-bottom: 14px; }
  .contact-band {
    background: var(--green);
    color: #fff;
    font-size: 10px;
    line-height: 1.6;
    padding: 8px 14px;
    font-weight: 600;
  }

  /* Cover */
  .panel--cover { padding: 0; display: flex; flex-direction: column; }
  .cover-brand { justify-content: center; padding: 22px 0 12px; }
  .cover-photo {
    flex: 1;
    background: linear-gradient(180deg, #f4f4f4 0%, #e7ece2 45%, #b9dcbc 100%);
  }
  .cover-band {
    background: var(--green);
    color: #fff;
    text-align: center;
    padding: 16px 16px 20px;
  }
  .cover-title {
    font-family: "Oswald", "Arial Narrow", sans-serif;
    font-weight: 400; font-size: 22px; letter-spacing: .5px;
    border-top: 1px solid rgba(255,255,255,.7);
    border-bottom: 1px solid rgba(255,255,255,.7);
    padding: 8px 0;
  }
  .cover-subtitle {
    font-family: "Oswald", "Arial Narrow", sans-serif;
    font-weight: 300; font-size: 15px; margin-top: 9px;
  }
</style>
</head>
<body>

  <div class="brand brand--hero">
    <span class="brand-dot"></span>
    <span class="brand-name">Marrowby Staffing</span>
  </div>

  <!-- Inside of the tri-fold -->
  <section class="spread spread--inside">
    <article class="panel">
      <h3 class="tag">What is a Pressure Ulcer?</h3>
      <p class="copy">A pressure ulcer is an area of damage to the skin and underlying tissue. They are sometimes known as pressure sores or bed sores.</p>
      <h3 class="tag">What causes a Pressure Ulcer?</h3>
      <p class="copy">Pressure ulcers are caused by poor circulation to tissues due to a combination of the following factors:</p>
      <h3 class="tag">Pressure</h3>
      <p class="copy">Body weight and some equipment (e.g. anti-thrombosis stockings) can squash the skin and other tissues where parts are under pressure. This reduces the blood supply to the area and can lead to tissue damage.</p>
      <h3 class="tag">Shearing</h3>
      <p class="copy">Sliding or slumping down the bed/chair can damage the skin and deeper layers of tissue.</p>
      <h3 class="tag">Friction</h3>
      <p class="copy">Poor moving and handling methods can remove or damage the top layers of skin. Repeated friction can injure the area.</p>
      <h3 class="tag">Who is most at risk</h3>
      <p class="copy">You may be at risk of developing a pressure ulcer for a number of reasons including:</p>
      <h3 class="tag">Problems with Movement</h3>
      <p class="copy">If your ability to move is limited, you cannot shift weight to restore blood and oxygen to the parts under pressure.</p>
      <h3 class="tag">Poor Circulation</h3>
      <p class="copy">Vascular disease or smoking reduces your blood flow and slows healing.</p>
    </article>

    <article class="panel">
      <h3 class="tag">Moist Skin</h3>
      <p class="copy">You may be at increased risk if your skin is too damp, due to incontinence, sweat or a weeping wound. It is important that your skin is kept clean and healthy.</p>
      <h3 class="tag">Lack of Sensitivity to Pain or Discomfort</h3>
      <p class="copy">Conditions such as Diabetes Stroke, Nerve, Muscle Disorders, etc. reduce the normal sensations that usually prompt you, or enable you to move. Some treatments (e.g. Epidural pain relief, medications, and operations) reduce your sensitivity to pain or discomfort so that you are not aware of the need to move.</p>
      <h3 class="tag">Previous Tissue Damage</h3>
      <p class="copy">Scar tissue will have lost some of its previous strength and is more prone to breakdown.</p>
      <h3 class="tag">Inadequate Diet or Fluid Intake</h3>
      <p class="copy">Poor diet can weaken and dehydrate your tissues, while weight changes alter pressure distribution on the skin.</p>
      <p class="copy" style="margin-top:8px">If you are developing Pressure Ulcers, talk to your care team as soon as possible. This will help them plan treatment and prevent further damage.</p>
    </article>

    <article class="panel">
      <p class="copy copy--lead">Without appropriate intervention the damage may worsen, developing into hard black tissue or an open wound.</p>
      <h3 class="tag locations-title">Common Locations of Pressure Ulcers</h3>

      <p class="pose-label">
        <svg width="14" height="8" viewBox="0 0 14 8" aria-hidden="true"><path d="M0 4h12M9 1l3 3-3 3" fill="none" stroke="currentColor" stroke-width="1.2"/></svg>
        Laying on your back
      </p>
      <div class="pose-figure" role="img" aria-label="Outline drawing of a person lying on their back with red markers at back of head, shoulder blade, elbow, coccyx and base of spine, and heel"></div>

      <p class="pose-label">
        <svg width="14" height="8" viewBox="0 0 14 8" aria-hidden="true"><path d="M0 4h12M9 1l3 3-3 3" fill="none" stroke="currentColor" stroke-width="1.2"/></svg>
        Laying on your side
      </p>
      <div class="pose-figure" role="img" aria-label="Outline drawing of a person lying on their side with red markers at thigh, lower leg, and heel and ankle"></div>

      <p class="pose-label">
        <svg width="14" height="8" viewBox="0 0 14 8" aria-hidden="true"><path d="M0 4h12M9 1l3 3-3 3" fill="none" stroke="currentColor" stroke-width="1.2"/></svg>
        Sitting in a chair
      </p>
      <div class="pose-figure" role="img" aria-label="Outline drawing of a person seated in a wheelchair with red markers at elbow, heel and ball of foot"></div>
    </article>
  </section>

  <!-- Outside of the tri-fold: back and cover -->
  <section class="spread spread--outside">
    <article class="panel panel--contact">
      <div class="contact-rotated">
        <div class="brand brand--small">
          <span class="brand-dot"></span>
          <span class="brand-name">Marrowby Staffing</span>
        </div>
        <h2 class="contact-heading">CONTACT US</h2>
        <p class="contact-name">Delia Hartwell</p>
        <p class="contact-role">- Clinical Nurse Lead</p>
        <div class="contact-band">
          delia.hartwell@marrowbystaffing.co.uk<br>
          www.marrowbystaffing.co.uk<br>
          T: 0203 000 4821
        </div>
      </div>
    </article>

    <article class="panel panel--cover">
      <div class="brand brand--small cover-brand">
        <span class="brand-dot"></span>
        <span class="brand-name">Marrowby Staffing</span>
      </div>
      <div class="cover-photo" role="img" aria-label="Photograph of a smiling nurse in mint green scrubs with a stethoscope, holding a clipboard"></div>
      <div class="cover-band">
        <h1 class="cover-title">PRESSURE AREA CARE</h1>
        <p class="cover-subtitle">Guide for patients</p>
      </div>
    </article>
  </section>

</body>
</html>
```